Job advertisement

A graphic job advertisement. It's supposed to be slightly different from the normal ads. Eye-catcher and later the text for the job description.

```html
<!DOCTYPE html>
<html lang="de">
<head>
<meta charset="utf-8">
<title>Stellenanzeige – elektro brandtner</title>
<link href="https://fonts.googleapis.com/css2?family=Exo+2:wght@400;500&family=Oswald:wght@700&display=swap" rel="stylesheet">
<style>
  :root {
    --page-bg: #e8eff7;
    --paper: #ffffff;
    --frame-grey: #8e9597;
    --brand-grey: #5d6466;
    --signal-red: #e30613;
    --glow-orange: #f08a00;
    --glow-yellow: #fcc70f;
    --ink-dark: #2a2d33;
  }
  html, body {
    margin: 0;
    width: 1200px;
    height: 1200px;
    overflow: hidden;
    background: var(--page-bg);
  }
  .job-poster {
    position: absolute;
    left: 197px;
    top: 30px;
    width: 806px;
    height: 1140px;
    display: block;
  }
  .poster-sheet { fill: var(--paper); }
  .poster-frame { fill: none; stroke: var(--frame-grey); stroke-width: 4; }
  .brand-name {
    font-family: "Exo 2", sans-serif;
    font-weight: 500;
    font-size: 50px;
    fill: var(--brand-grey);
  }
  .brand-dot { fill: var(--signal-red); }
  .term-ring {
    font-family: "Oswald", sans-serif;
    font-weight: 700;
    font-size: 52px;
    letter-spacing: 1px;
    fill: var(--signal-red);
  }
  .term-separator { fill: var(--ink-dark); }
  .footer-hill { fill: var(--signal-red); }
  .call-to-action {
    font-family: "Exo 2", sans-serif;
    font-weight: 400;
    font-size: 26px;
    fill: var(--paper);
  }
</style>
</head>
<body>
<svg class="job-poster" viewBox="0 0 834 1180" xmlns="http://www.w3.org/2000/svg">
  <defs>
    <radialGradient id="lantern-glow" cx="50%" cy="50%" r="50%">
      <stop offset="0%" stop-color="#fce9a0"/>
      <stop offset="40%" stop-color="var(--glow-yellow)"/>
      <stop offset="70%" stop-color="var(--glow-orange)"/>
      <stop offset="100%" stop-color="var(--signal-red)"/>
    </radialGradient>
    <path id="term-circle" d="M 417 925 A 295 295 0 1 1 417 335 A 295 295 0 1 1 417 925"/>
  </defs>

  <rect class="poster-sheet" x="0" y="0" width="834" height="1180"/>
  <rect class="poster-frame" x="22" y="22" width="790" height="1135"/>

  <g class="brand">
    <circle class="brand-dot" cx="232" cy="124" r="30"/>
    <text class="brand-name" x="280" y="142">elektro brandtner</text>
  </g>

  <path class="footer-hill" d="M 37 1015 C 160 940 300 925 417 925 C 560 925 700 960 797 1035 L 797 1140 L 37 1140 Z"/>

  <circle class="hero-illustration" cx="417" cy="630" r="255" fill="url(#lantern-glow)"
          role="img" aria-label="Illustration: dunkle Sturmlaterne mit rotem Blitzsymbol vor einer leuchtenden Sonne in Rot, Orange und Gelb"/>

  <text class="term-ring">
    <textPath href="#term-circle" startOffset="12.5%" text-anchor="middle">STROM</textPath>
  </text>
  <text class="term-ring">
    <textPath href="#term-circle" startOffset="23%" text-anchor="middle">VOLT</textPath>
  </text>
  <text class="term-ring">
    <textPath href="#term-circle" startOffset="35.5%" text-anchor="middle">SPANNUNG</textPath>
  </text>
  <text class="term-ring">
    <textPath href="#term-circle" startOffset="50%" text-anchor="middle">OHM</textPath>
  </text>
  <text class="term-ring">
    <textPath href="#term-circle" startOffset="61.5%" text-anchor="middle">AMPERE</textPath>
  </text>
  <text class="term-ring">
    <textPath href="#term-circle" startOffset="73%" text-anchor="middle">WATT</textPath>
  </text>
  <text class="term-ring">
    <textPath href="#term-circle" startOffset="85.3%" text-anchor="middle">LEISTUNG</textPath>
  </text>

  <circle class="term-separator" cx="135" cy="760" r="9"/>
  <circle class="term-separator" cx="104" cy="580" r="9"/>
  <circle class="term-separator" cx="710" cy="495" r="9"/>
  <circle class="term-separator" cx="725" cy="692" r="9"/>

  <text class="call-to-action" x="417" y="1060" text-anchor="middle">Wir suchen SIE! Power-Worker Bewerbung an:</text>
  <text class="call-to-action" x="417" y="1099" text-anchor="middle">personal@elektrobrandtner.de</text>
</svg>
</body>
</html>
```